RQ Alarm 'Welcome' Envelope

I am looking for a 'Welcome' envelope design for new customers who sign up for our Alarm Services. In this envelope we will send confidential documents that the customer will need. I want it to stand out, yet look classy.

```html
<!DOCTYPE html>
<html lang="en">
<head>
<meta charset="utf-8">
<title>RQ Alarm Welcome Envelopes</title>
<link rel="stylesheet" href="https://fonts.googleapis.com/css2?family=Montserrat:wght@500;600;700&display=swap">
<style>
  :root {
    --backdrop: #e6e1d8;
    --kraft: #e3a850;
    --kraft-edge: #c98f3b;
    --paper: #f4f4f2;
    --paper-edge: #d6d6d3;
    --brand-blue: #1c3f9a;
    --brand-green: #22a81f;
    --ink: #2a2a2a;
    --rule: #1f2d5c;
  }
  * { margin: 0; padding: 0; box-sizing: border-box; }
  html, body { width: 1200px; height: 854px; overflow: hidden; }
  body {
    background: var(--backdrop);
    font-family: "Montserrat", Arial, sans-serif;
    color: var(--ink);
    position: relative;
  }
  .brand-name {
    font-weight: 700;
    color: var(--brand-blue);
    display: flex; align-items: center; gap: 6px;
    letter-spacing: 0.5px;
    line-height: 1;
  }
  .brand-mark { display: inline-block; background: var(--brand-green); }
  .tagline {
    font-weight: 700; letter-spacing: 0.6px;
    text-transform: uppercase; color: var(--ink);
    white-space: nowrap;
  }
  .contact-line {
    display: flex; gap: 14px;
    font-size: 7px; font-weight: 500; letter-spacing: 0.4px;
    white-space: nowrap;
  }

  .catalog-envelope {
    position: absolute;
    left: 70px; top: 77px;
    width: 520px; height: 700px;
    background: var(--kraft);
    border: 1px solid var(--kraft-edge);
  }
  .catalog-envelope .flap { position: absolute; left: 0; top: 0; }
  .catalog-footer {
    position: absolute;
    left: 38px; right: 38px; bottom: 58px;
  }
  .catalog-footer .brand-row {
    display: flex; align-items: flex-end; justify-content: space-between;
    border-bottom: 1px solid var(--kraft-edge);
    padding-bottom: 5px;
  }
  .catalog-footer .brand-name { font-size: 22px; }
  .catalog-footer .brand-mark { width: 10px; height: 10px; }
  .catalog-footer .tagline { font-size: 6.5px; }
  .catalog-footer .contact-line { margin-top: 7px; }

  .business-envelope {
    position: absolute;
    left: 610px; top: 300px;
    width: 540px; height: 236px;
    background: var(--paper);
    border: 1px solid var(--paper-edge);
  }
  .business-envelope .flap { position: absolute; left: 0; top: 0; }
  .business-envelope .brand-block { position: absolute; left: 28px; top: 42px; }
  .business-envelope .brand-name { font-size: 24px; }
  .business-envelope .brand-mark { width: 11px; height: 11px; }
  .business-envelope .tagline { font-size: 5.5px; margin-top: 6px; }
  .business-envelope .contact-block {
    position: absolute; left: 28px; right: 60px; bottom: 18px;
  }
  .contact-block .rule { height: 1px; background: var(--rule); margin-bottom: 6px; }
</style>
</head>
<body>
  <section class="catalog-envelope" aria-label="Kraft catalog envelope">
    <svg class="flap" width="520" height="120" viewBox="0 0 520 120" aria-hidden="true">
      <path d="M2 4 L18 86 Q22 106 44 106 L478 106 Q500 106 504 86 L518 4" fill="none" stroke="var(--kraft-edge)" stroke-width="1.4"/>
    </svg>
    <div class="catalog-footer">
      <div class="brand-row">
        <span class="brand-name"><span class="brand-mark"></span>RQ Alarm</span>
        <span class="tagline">Peace of mind, day and night</span>
      </div>
      <div class="contact-line">
        <span>PO Box 2270, Harbor Point, WA 98012</span>
        <span>|</span>
        <span>care@rqalarm.net</span>
        <span>|</span>
        <span>P: 888-555-0142</span>
      </div>
    </div>
  </section>

  <section class="business-envelope" aria-label="White business envelope">
    <svg class="flap" width="540" height="40" viewBox="0 0 540 40" aria-hidden="true">
      <path d="M2 2 L14 20 Q18 26 28 26 L502 26 Q512 26 516 20 L538 2" fill="none" stroke="var(--paper-edge)" stroke-width="1.2"/>
    </svg>
    <div class="brand-block">
      <span class="brand-name"><span class="brand-mark"></span>RQ Alarm</span>
      <div class="tagline">Peace of mind, day and night</div>
    </div>
    <div class="contact-block">
      <div class="rule"></div>
      <div class="contact-line">
        <span>PO Box 2270, Harbor Point, WA 98012</span>
        <span>|</span>
        <span>care@rqalarm.net</span>
        <span>|</span>
        <span>P: 888-555-0142</span>
      </div>
    </div>
  </section>
</body>
</html>
```